Stylist/Barber Standup Sign for Hair Regrowth Company

We want to design an attractive and eye-catching sign for hair stylists and barbers to sit on their workstations to attract the attention of their clients regarding hair loss and encourage them to speak to their stylist about it of they are would like to seek treatment.
50% of men and 25% of women suffer from hair loss but most are in denial that it is happening or too embarrassed to talk about it.

Copy for the flyer is as follows:

[Section 1:]
This flyer has been placed here/designed to spark conversation about hair loss

[Section 2:]
The truth is...
73% of people believe their hair is thinning
They are right

[Section 3:]
If you've got questions, your stylist or barber has answers.

Additional Background Information:

Primary target audience is men between the ages of 25-45, secondary target audience is men 46-60

Current Consumer Perception? (in the first person) “I’ve been thinking about my hair. I think it’s getting thinner and I’m scared, worried and don’t know what to do. But I don’t know if there is anything that really works. I’ve tried other things and nothing‘s worked.”

Tonality of materials? Very guy friendly, matter of fact, authoritative, its what you might hear from your best friend. Confident. Encouraging, but with a sense of urgency.

Please use our brand colors, but do not include our logo or brand name.
Colors are as follows:
Green: #4ca26f
Light Grey: #999999
Dark Grey: #262626

I have attached print templates in both PDF and Jpeg, please use those to provide final ready to print documents if you are selected.

Target Market(s)

Industry/Entity Type

Health And Wellness

Font styles to use
Sans Serif

Colors
00a990
ffffff
333333
cbcbcb

Requirements
Must have
• We want to get across the following messaging. Ideally you will submit a design using our copy and if you think you can do better, please feel free to submit another design with your own copy/messaging. If you can do it better we would love to select you :-)
• Our copy?
• This flyer has been placed here/designed to spark conversation about hair loss
• The truth is...
• 73% of people believe their hair is thinning
• They are right
• If you've got questions, your stylist or barber has answers
• Also please use our brand colors:
• Green: #4ca26f
• Light Grey: #999999
• Dark Grey: #262626
Should not have
• dont add any logos, images or ornate design. this needs to be simple, easy to ready and eye catching.
• do not use the color red in any capacity.

```html
<!DOCTYPE html>
<html lang="en">
<head>
<meta charset="utf-8">
<title>Hair Loss Conversation Sign</title>
<link rel="stylesheet" href="https://fonts.googleapis.com/css2?family=Cabin:wght@400&family=Cabin+Condensed:wght@400&display=swap">
<style>
  :root {
    --bg: #333333;
    --accent: #00a990;
    --ink: #ffffff;
  }
  html, body {
    margin: 0;
    padding: 0;
    overflow: hidden;
    background: var(--bg);
  }
  .sign {
    position: relative;
    width: 806px;
    height: 1200px;
    background: var(--bg);
    color: var(--ink);
    font-family: "Cabin", sans-serif;
    font-weight: 400;
    overflow: hidden;
  }
  .divider {
    position: absolute;
    left: 164px;
    width: 478px;
    height: 20px;
  }
  .divider--top { top: 99px; }
  .divider--bottom { top: 1081px; }
  .line {
    position: absolute;
    left: 0;
    width: 100%;
    margin: 0;
    text-align: center;
    white-space: nowrap;
    line-height: 1;
    transform: translateY(-50%);
  }
  .accent { color: var(--accent); }
  .intro-title { top: 204px; font-size: 50px; }
  .intro-body { font-size: 39px; }
  .intro-body--one { top: 280px; }
  .intro-body--two { top: 356px; }
  .truth {
    font-family: "Cabin Condensed", sans-serif;
  }
  .truth-lead {
    top: 521px;
    left: 46px;
    width: auto;
    text-align: left;
    font-size: 54px;
  }
  .truth-stat { top: 619px; font-size: 37px; }
  .truth-verdict {
    top: 706px;
    left: auto;
    right: 57px;
    width: auto;
    text-align: right;
    font-size: 37px;
  }
  .closing { font-size: 39px; }
  .closing--one { top: 928px; }
  .closing--two { top: 1001px; }
</style>
</head>
<body>
<main class="sign">
  <svg class="divider divider--top" viewBox="0 0 478 20" aria-hidden="true">
    <path d="M0 10 Q120 7 225 9 L239 3 L253 9 Q358 7 478 10 Q358 13 253 11 L239 17 L225 11 Q120 13 0 10 Z" fill="#00a990"/>
  </svg>

  <p class="line intro-title accent">This flyer</p>
  <p class="line intro-body intro-body--one">has been placed here/designed to</p>
  <p class="line intro-body intro-body--two"><span class="accent">spark</span> conversation about hair loss</p>

  <p class="line truth truth-lead">The truth is...</p>
  <p class="line truth truth-stat"><span class="accent">73%</span> of people believe their hair is thinning</p>
  <p class="line truth truth-verdict">They are right</p>

  <p class="line closing closing--one">If you've got questions,</p>
  <p class="line closing closing--two">your stylist or barber has answers.</p>

  <svg class="divider divider--bottom" viewBox="0 0 478 20" aria-hidden="true">
    <path d="M0 10 Q120 7 225 9 L239 3 L253 9 Q358 7 478 10 Q358 13 253 11 L239 17 L225 11 Q120 13 0 10 Z" fill="#00a990"/>
  </svg>
</main>
</body>
</html>
```